Bright Meadow Counseling Business Card design with a visually interesting use of Space

I need business cards that are luxurious and give a peaceful, calm vibe. I also had some letterhead designed, and i like the look of it also, it's attached with the logo design for reference/ ideas but feel free to be creative.

Target Market(s)

High end luxurious client who needs counseling

Industry/Entity Type

Marriage and Family Therapy

Contact Information for Business Card

Mira Kowalczyk MS LMFT/ or Toby Hallett address 4150 Larkin Suite 600

Font styles to use
Sans Serif

Colors
0054AA
0677BA
7BADD7
CADEEF
E8F1F8
0094D4
00A9DD
6FCCEA
C7EBF8
E9F6FB
A7469A
B969AE
D3A5CF
EDDBEB
F8F0F9
6B429C
8869AF
B7A5CE
E3DAEB
F3F0F8

Requirements
Must have
• Logo and color scheme but be simple modern and luxurious
Nice to have
• I'd like to incorporate some elelmets from the logo and letterhead into a simple modern card

```html
<!DOCTYPE html>
<html lang="en">
<head>
<meta charset="utf-8">
<title>Bright Meadow Counseling – Business Card</title>
<link href="https://fonts.googleapis.com/css2?family=Quicksand:wght@300;400;500;700&display=swap" rel="stylesheet">
<style>
  :root {
    --backdrop: #d6d6d6;
    --paper: #ffffff;
    --ink: #1b1b1b;
    --purple: #6b429c;
    --magenta: #a7469a;
    --teal: #2bbcc4;
    --teal-light: #34bcc6;
    --teal-deep: #247f90;
    --mist: #e9f6fb;
    --shadow: rgba(0, 0, 0, 0.18);
  }
  * { margin: 0; padding: 0; box-sizing: border-box; }
  html, body {
    width: 1200px;
    height: 846px;
    overflow: hidden;
    background: var(--backdrop);
    font-family: "Quicksand", sans-serif;
  }
  .canvas {
    position: relative;
    width: 1200px;
    height: 846px;
  }
  .card {
    position: absolute;
    top: 268px;
    width: 530px;
    height: 310px;
    border-radius: 2px;
    box-shadow: 0 10px 26px var(--shadow);
    overflow: hidden;
  }

  /* Front */
  .card-front {
    left: 50px;
    background: var(--paper);
    color: var(--ink);
  }
  .brand {
    position: absolute;
    left: 46px;
    top: 44px;
    display: flex;
    align-items: center;
    gap: 18px;
  }
  .brand-dot {
    width: 46px;
    height: 46px;
    border-radius: 50%;
    background: var(--magenta);
    opacity: 0.8;
    flex: none;
  }
  .brand-name {
    font-weight: 300;
    font-size: 40px;
    line-height: 1;
    letter-spacing: 0.5px;
    color: var(--ink);
  }
  .brand-name .brand-sub {
    display: block;
    margin-top: 6px;
    margin-left: 96px;
    font-size: 22px;
    letter-spacing: 4px;
  }
  .person {
    position: absolute;
    left: 46px;
    top: 176px;
    font-size: 22px;
    white-space: nowrap;
  }
  .person-name {
    font-weight: 700;
    color: var(--purple);
  }
  .person-title {
    font-weight: 400;
    font-size: 15px;
    color: var(--ink);
    margin-left: 4px;
  }
  .address {
    position: absolute;
    right: 30px;
    top: 160px;
    text-align: right;
    font-size: 15px;
    line-height: 1.35;
    font-weight: 400;
  }
  .rule {
    position: absolute;
    left: 46px;
    top: 210px;
    width: 454px;
    height: 5px;
  }
  .contact-list {
    position: absolute;
    left: 46px;
    top: 228px;
    list-style: none;
    font-size: 15px;
    line-height: 1.6;
  }
  .contact-list li {
    display: flex;
    align-items: center;
    gap: 9px;
  }
  .contact-icon { width: 16px; height: 16px; flex: none; }

  /* Back */
  .card-back {
    left: 620px;
    background: radial-gradient(ellipse at 45% 45%, var(--teal-light) 0%, #2ca3b2 45%, var(--teal-deep) 100%);
    color: #ffffff;
  }
  .back-dot {
    position: absolute;
    right: 74px;
    top: 34px;
    width: 96px;
    height: 96px;
    border-radius: 50%;
    background: var(--mist);
    opacity: 0.75;
  }
  .back-name {
    position: absolute;
    left: 48px;
    top: 142px;
    font-weight: 300;
    font-size: 56px;
    line-height: 1;
    letter-spacing: 0.5px;
  }
  .back-web {
    position: absolute;
    left: 90px;
    top: 222px;
    font-weight: 500;
    font-size: 13px;
    letter-spacing: 1.5px;
  }
</style>
</head>
<body>
<main class="canvas">

  <section class="card card-front" aria-label="Business card front">
    <div class="brand">
      <span class="brand-dot" aria-hidden="true"></span>
      <h1 class="brand-name">Bright Meadow<span class="brand-sub">Counseling</span></h1>
    </div>

    <p class="person"><span class="person-name">Mira Kowalczyk</span><span class="person-title">MS LMFT</span></p>

    <p class="address">4150 Larkin Ave<br>Dallas, TX 75230</p>

    <svg class="rule" viewBox="0 0 454 5" preserveAspectRatio="none" aria-hidden="true">
      <rect x="0" y="0" width="150" height="5" fill="var(--purple)"/>
      <rect x="154" y="0" width="150" height="5" fill="var(--magenta)"/>
      <rect x="308" y="0" width="146" height="5" fill="var(--teal)"/>
    </svg>

    <ul class="contact-list">
      <li>
        <svg class="contact-icon" viewBox="0 0 16 16" aria-hidden="true">
          <rect x="3.5" y="1" width="9" height="14" rx="1.5" fill="none" stroke="var(--teal)" stroke-width="1.6"/>
          <line x1="6.5" y1="12.5" x2="9.5" y2="12.5" stroke="var(--teal)" stroke-width="1.4"/>
        </svg>
        <span>214 555 0142</span>
      </li>
      <li>
        <svg class="contact-icon" viewBox="0 0 16 16" aria-hidden="true">
          <rect x="1" y="3" width="14" height="10" rx="1" fill="var(--teal)"/>
          <polyline points="1.5,3.8 8,9 14.5,3.8" fill="none" stroke="#ffffff" stroke-width="1.3"/>
        </svg>
        <span>mira@brightmeadowcounseling.com</span>
      </li>
    </ul>
  </section>

  <section class="card card-back" aria-label="Business card back">
    <span class="back-dot" aria-hidden="true"></span>
    <h2 class="back-name">Bright Meadow</h2>
    <p class="back-web">WWW.BRIGHTMEADOWCOUNSELING.COM</p>
  </section>

</main>
</body>
</html>
```